New Stationery New Logo for KT Mouldings Limited

We have a new logo and now want new stationary to go with it

This will be

Letterhead
Compliments Slip
Business Cards

Company details are
KT Mouldings Limited
Brindle Row, Rugby, Warwickshire, CV34 7HX, UK
Telephone : +44(0)1788 930467
Fax: +44(0)1788 918723
Email: sales@ktmouldings.example
Web: www.ktmouldings.example

Target Market(s)

Engineering / Metal Stamping

Industry/Entity Type

Manufacture

Contact Information for Business Card

Neil Garbutt
Business Development Manager
KT Mouldings Limited
Brindle Row
Rugby
Warwickshire
CV34 7HX, UK

T: +44(0)1788 930467
F: +44(0)1788 918723
E: sales@ktmouldings.example
W: www.ktmouldings.example

Font styles to use
Sans Serif

Colors
33a6d7
0555a3
3176b5
85cae6
85acd3

Requirements
Must have
• Logo

```html
<!DOCTYPE html>
<html lang="en">
<head>
<meta charset="utf-8">
<title>KT Mouldings – Business Card</title>
<link rel="stylesheet" href="https://fonts.googleapis.com/css2?family=Open+Sans:wght@300;400;600;700&display=swap">
<style>
  :root {
    --brand-blue: #0b4ea2;
    --brand-blue-deep: #063f88;
    --brand-mid: #3176b5;
    --brand-light: #85cae6;
    --card-white: #ffffff;
    --page-bg: #e9ecef;
    --divider: #1d2a3a;
  }
  * { margin: 0; padding: 0; box-sizing: border-box; }
  html, body {
    width: 1200px; height: 950px; overflow: hidden;
    background: var(--page-bg);
    font-family: "Open Sans", Arial, sans-serif;
  }
  .canvas {
    position: relative; width: 1200px; height: 950px;
  }
  .card {
    position: absolute; left: 280px;
    width: 640px; height: 366px;
    overflow: hidden;
    box-shadow: 0 8px 24px rgba(0,0,0,.18);
  }
  .card-front { top: 80px; background: var(--card-white); }
  .card-back  { top: 504px; background: var(--brand-blue); }

  /* front */
  .front-panel { position: absolute; inset: 0; }
  .brand {
    position: absolute; left: 0; top: 0; width: 300px; height: 366px;
    display: flex; align-items: center; justify-content: center; gap: 10px;
  }
  .brand-name {
    color: var(--brand-mid);
    font-weight: 400; font-size: 22px; letter-spacing: 5px;
    text-transform: uppercase;
  }
  .brand-dot {
    width: 12px; height: 12px; border-radius: 50%;
    background: var(--brand-mid);
  }
  .details {
    position: absolute; left: 340px; top: 46px; color: #fff;
  }
  .person-name { font-weight: 700; font-size: 24px; letter-spacing: .5px; line-height: 1.1; }
  .person-role { font-weight: 300; font-size: 14px; letter-spacing: .5px; margin-top: 2px; }
  .company { font-weight: 700; font-size: 14px; margin-top: 22px; }
  .address { font-weight: 400; font-size: 13px; line-height: 1.45; }
  .contacts { list-style: none; margin-top: 14px; font-size: 13px; line-height: 1.55; }
  .contacts li { display: flex; align-items: center; gap: 9px; }
  .contacts svg { width: 13px; height: 13px; fill: #fff; flex: none; }

  /* back */
  .back-pattern { position: absolute; inset: 0; background: linear-gradient(135deg, #0d55ab, var(--brand-blue-deep)); }
  .back-name {
    position: absolute; left: 300px; bottom: 46px;
    color: #fff; font-weight: 400; font-size: 18px; letter-spacing: 4px; text-transform: uppercase;
  }
</style>
</head>
<body>
<main class="canvas">

  <section class="card card-front" aria-label="Business card front">
    <svg class="front-panel" viewBox="0 0 640 366" width="640" height="366" aria-hidden="true">
      <polygon points="300,0 640,0 640,366 300,366 300,92 286,76 300,60" fill="var(--brand-blue)"/>
      <polyline points="300,0 300,60 286,76 300,92 300,366" fill="none" stroke="var(--divider)" stroke-width="3"/>
    </svg>

    <div class="brand">
      <span class="brand-name">KT Mouldings</span>
      <span class="brand-dot"></span>
    </div>

    <div class="details">
      <p class="person-name">TOM HARLOW</p>
      <p class="person-role">CEO/FOUNDER</p>
      <p class="company">KT Mouldings Limited</p>
      <p class="address">Brindle Row, Rugby<br>Warwickshire, CV34 7HX, UK</p>
      <ul class="contacts">
        <li>
          <svg viewBox="0 0 16 16"><path d="M3.6 1.2l2.2 2.6-1.2 1.8c.9 2 2.6 3.8 4.7 4.8l1.8-1.2 2.7 2.1-1.1 2.8C7.2 14.8 1.2 8.8 1 2.4z"/></svg>
          +44(0)1788 930467
        </li>
        <li>
          <svg viewBox="0 0 16 16"><rect x="4" y="1" width="8" height="5"/><rect x="1" y="6" width="14" height="6" rx="1"/><rect x="4" y="11" width="8" height="4"/></svg>
          +44(0)1788 918723
        </li>
        <li>
          <svg viewBox="0 0 16 16"><path d="M1 3h14v10H1z M1.5 3.5L8 9l6.5-5.5" stroke="#0b4ea2" stroke-width="1"/></svg>
          sales@ktmouldings.example
        </li>
        <li>
          <svg viewBox="0 0 16 16"><circle cx="8" cy="8" r="7"/><path d="M1 8h14M8 1c-3 3.5-3 10.5 0 14M8 1c3 3.5 3 10.5 0 14" stroke="#0b4ea2" stroke-width="1" fill="none"/></svg>
          www.ktmouldings.example
        </li>
      </ul>
    </div>
  </section>

  <section class="card card-back" aria-label="Business card back">
    <div class="back-pattern" role="img" aria-label="Faint repeating brand pattern in light blue tones"></div>
    <p class="back-name">KT Mouldings</p>
  </section>

</main>
</body>
</html>
```